Coffee bag and coffee beer revamp

We need a coffee bag design where we can print two stickers and they fit nicely on the bag. this is an example of 500gr bag. We will also need 250gr and 1kilo versions.

One the logo attached and the other the coffee description details attached.
This should sit nicely on the white bag example attached.
One is also a photo of what we have but it needed some work to make sure dimensions are good and its clear.
Example: attached of text and these will be variable values that we need the label to edit and they should be different colour labels - we have 6 types of coffee.

<COFFEE TYPE> example House BLEND
<DATE ROASTED> 17/03/23
Text always the same -- "Consume within 12 months"

I have also attache the font and original files. There can be some colour added.

Other types of coffee

SIDAMO
GUATEMALA
SANTOS
COSTA RICA
SUPREMO
DECAF

The beer is just the logo and text "Delvana Cold Brew Coffee" label with the date and logo.

Target Market(s)

coffee lovers

Industry/Entity Type

food

Font styles to use
Other font styles liked:
• i will upload the fonts

Colors
EB3D1F
EC4F4E
F09395
F8D3D4
FCEDEE

Requirements
Nice to have
• can try alternative colour? even just for labels

```html
<!DOCTYPE html>
<html lang="en">
<head>
<meta charset="utf-8">
<title>Delvana Cold Brew Coffee – Front Label</title>
<link rel="stylesheet" href="https://fonts.googleapis.com/css2?family=Work+Sans:wght@600;700&family=Oswald:wght@500&display=swap">
<style>
  :root {
    --backdrop: #e4e4e2;
    --label-black: #0d0b0c;
    --label-edge: #1c1819;
    --ink-white: #f1f0ee;
    --ink-soft: #dcdad7;
  }
  html, body {
    margin: 0;
    padding: 0;
    width: 1200px;
    height: 1200px;
    overflow: hidden;
    background: var(--backdrop);
  }
  .canvas {
    position: relative;
    width: 1200px;
    height: 1200px;
    display: flex;
    align-items: center;
    justify-content: center;
  }
  .front-label {
    width: 720px;
    height: 1060px;
    background: var(--label-black);
    border: 2px solid var(--label-edge);
    border-radius: 28px;
    box-sizing: border-box;
    display: flex;
    flex-direction: column;
    align-items: center;
    padding-top: 160px;
    color: var(--ink-white);
    font-family: "Work Sans", Arial, sans-serif;
  }
  .front-label p,
  .front-label h1 {
    margin: 0;
  }
  .brand {
    display: flex;
    align-items: center;
    gap: 16px;
    margin-bottom: 110px;
    line-height: 1;
  }
  .brand-name {
    font-weight: 600;
    font-size: 56px;
    letter-spacing: 4px;
    color: var(--ink-soft);
  }
  .brand-dot {
    width: 16px;
    height: 16px;
    border-radius: 50%;
    background: var(--ink-soft);
  }
  .product-title {
    text-align: center;
    font-weight: 700;
    line-height: 0.95;
  }
  .product-title .line-main {
    display: block;
    font-size: 150px;
    letter-spacing: 2px;
  }
  .product-title .line-sub {
    display: block;
    font-size: 72px;
    font-weight: 600;
    letter-spacing: 5px;
    margin-top: 18px;
    line-height: 1;
    color: var(--ink-soft);
  }
  .blend-name {
    margin-top: 70px !important;
    font-weight: 700;
    font-size: 30px;
    line-height: 1;
    letter-spacing: 1.5px;
    color: var(--ink-soft);
  }
  .volume {
    margin-top: 60px !important;
    font-family: "Oswald", "Arial Narrow", sans-serif;
    font-weight: 500;
    font-size: 22px;
    line-height: 1;
    letter-spacing: 1.5px;
    color: var(--ink-soft);
  }
</style>
</head>
<body>
  <main class="canvas">
    <section class="front-label" aria-label="Delvana Cold Brew Coffee front label">
      <div class="brand">
        <span class="brand-name">DELVANA</span>
        <span class="brand-dot" aria-hidden="true"></span>
      </div>
      <h1 class="product-title">
        <span class="line-main">COLD</span>
        <span class="line-main">BREW</span>
        <span class="line-sub">COFFEE</span>
      </h1>
      <p class="blend-name">HOUSE BLEND</p>
      <p class="volume">10.5 FL OZ (310 ML)</p>
    </section>
  </main>
</body>
</html>
```